PowerPoint template for online medical education

Need a PowerPoint design for our online urgent care education content Need a title page and then further pages.

must have our logo, name and tagline Institute of Rapid Clinic Practice
Elevating Care, Empowering Clinicians
Should match our logo colors scheme

enclosed our logo, tagline ans a copy of our newsletter

Target Market(s)

PHYSICIANS, and other professionals

Industry/Entity Type

Medicine

Font styles to use
Serif

Requirements
Must have
• our logo
• tagline
• color scheme like our logo
Should not have
• too much on content pages

```html
<!DOCTYPE html>
<html lang="en">
<head>
<meta charset="utf-8">
<title>Institute of Rapid Clinic Practice – Presentation Template</title>
<link href="https://fonts.googleapis.com/css2?family=Roboto:ital,wght@0,400;0,700;1,700&family=Raleway:wght@400;500&display=swap" rel="stylesheet">
<style>
  :root{
    --stage:#5f5a58;
    --orange:#f0a13f;
    --red:#b8412a;
    --white:#ffffff;
    --ink:#6a6a6a;
    --ink-dark:#4a4a4a;
    --photo-skin:#c9a58c;
    --photo-sheet:#8fa3bf;
  }
  *{margin:0;padding:0;box-sizing:border-box}
  html,body{width:1200px;height:1200px;overflow:hidden;background:var(--stage)}
  body{position:relative;font-family:"Roboto",Arial,sans-serif;color:var(--ink)}
  .slide{position:absolute;width:434px;height:334px;background:var(--white);overflow:hidden}
  .s-case{left:86px;top:64px}
  .s-lyme-refs{left:676px;top:64px}
  .s-bells{left:86px;top:434px}
  .s-contact{left:674px;top:434px;width:438px}
  .s-member{left:86px;top:808px}
  .s-title{left:674px;top:808px;width:438px}
  .top-band{position:absolute;left:0;top:0;width:100%;height:19px;background:var(--orange)}
  .foot-band{position:absolute;left:0;bottom:0;width:100%;height:14px}
  .foot-band svg{position:absolute;left:0;top:0}
  .foot-label{position:absolute;left:29px;top:1px;font-size:9px;font-weight:700;color:var(--white);letter-spacing:.1px;white-space:nowrap}
  .accent-bar{position:absolute;left:0;top:170px}
  .body-text{position:absolute;font-size:5.9px;line-height:1.25;text-align:justify;color:var(--ink)}
  .body-text p{margin-bottom:4px}
  .body-text h4{font-size:6px;font-weight:700;color:var(--ink-dark)}
  .photo{position:absolute;border-radius:1px}
  .caption{position:absolute;left:40px;top:276px;width:365px;font-size:6px;line-height:1.3;text-align:right}
  .red-block{position:absolute;left:0;top:20px;width:100%;background:var(--red)}
  .brand{position:absolute;display:flex;align-items:center;gap:8px}
  .brand-mark{border-radius:50%;background:var(--white)}
  .brand-name{font-family:"Raleway",Arial,sans-serif;font-variant:small-caps;color:var(--white);letter-spacing:.8px;line-height:1.05}
  .rule{position:absolute;background:var(--white)}
  .about{position:absolute;left:30px;top:132px;width:379px;font-size:5.9px;font-weight:700;line-height:1.3;color:var(--white);text-align:justify}
  .about h3{text-align:center;font-size:8px;margin:4px 0 1px}
  .contact-list{position:absolute;left:77px;top:225px;list-style:none}
  .contact-list li{display:flex;align-items:center;gap:8px;font-size:6px;font-weight:700;color:var(--ink-dark);height:15px;line-height:1.2}
  .contact-list li svg{flex:none}
  .site-url{position:absolute;right:28px;top:259px;font-size:20px;font-weight:700;color:var(--red)}
  .kicker{font-size:7px;font-weight:700;color:var(--ink)}
  .headline{font-size:7px;font-weight:700;color:#222;margin-bottom:6px}
  .tagline{position:absolute;left:185px;top:252px;font-size:9px;font-weight:700;font-style:italic;color:#fbe5c8}
</style>
</head>
<body>

<section class="slide s-case">
  <div class="top-band"></div>
  <div class="photo" role="img" aria-label="Clinical photo: legs with urticarial rash" style="left:20px;top:47px;width:109px;height:103px;background:linear-gradient(160deg,#e9e6e2,var(--photo-skin))"></div>
  <div class="photo" role="img" aria-label="Clinical photo: close-up of red patches on skin" style="left:134px;top:47px;width:109px;height:103px;background:linear-gradient(150deg,#d9b39a,#b8735f)"></div>
  <div class="photo" role="img" aria-label="Clinical photo: lower legs on hospital sheet" style="left:20px;top:158px;width:109px;height:103px;background:linear-gradient(130deg,var(--photo-sheet),var(--photo-skin))"></div>
  <div class="photo" role="img" aria-label="Clinical photo: knee with scattered lesions" style="left:134px;top:158px;width:109px;height:103px;background:linear-gradient(140deg,var(--photo-sheet),#c79a82)"></div>
  <div class="body-text" style="left:253px;top:47px;width:151px">
    Patient was discharged with a 14 day Prednisone taper and NSAIDS. Follow up with Dermatology.
    Discussion: Urticarial vasculitis is an urticarial eruption that is often painful or has a burning sensation prior to the eruption of lesions. Lesions are red patches or plaques and petechiae may appear. They usually last for more than 24 hours and then as lesions resolve an area of ecchymosis is present. The cause of the lesions is usually unknown but can be associated with SLE, Sjogren syndrome, leukemia, viral disease such as Hepatitis B/C and can also be drug-induced from ACE inhibitors, PCN, sulfonamides, fluoxetine and thiazides. The majority are idiopathic.
  </div>
  <p class="caption">Have an interesting case or just want to let others know about an unusual diagnosis, send it our way. It does not have to be this large or extensive. Just be sure to remove all PHI and we will share it with the institute.</p>
  <div class="foot-band">
    <svg width="434" height="14"><rect width="434" height="14" fill="var(--orange)"/><polygon points="274,0 434,0 434,14 259,14" fill="var(--red)"/></svg>
    <span class="foot-label">INSTITUTE OF RAPID CLINIC PRACTICE</span>
  </div>
</section>

<section class="slide s-lyme-refs">
  <div class="top-band"></div>
  <div class="body-text" style="left:164px;top:48px;width:243px">
    <p>States with the highest rates of Lyme disease are Connecticut, Delaware, Maine, Maryland, Minnesota, New Hampshire, New Jersey, New York, Pennsylvania, Rhode Island, Virginia, Vermont and Wisconsin.
    The infected tick needs to be attached for approximately 36 hours to transmit the B. burgdorferi spirochete. If the patient has symptoms of an infection such as an erythema migrans rash, fever or joint pain, the treatment is extended. This single dose regimen is for the patient without symptoms, whom meets all the criteria stated. No alternative medications are recommended for pregnant patients, children less than 8 years old or doxycycline allergic patients currently.</p>
    <p>National Health Bureau (2012). Tickborne Diseases of the United States. Accessed on September 26, 2017. Journal of Field Infection Review, Volume 43, Issue 9, November 2006, Pages 1089–1134. Review of the clinical assessment, treatment and prevention of Lyme disease. Accessed on September 26, 2017.</p>
  </div>
  <svg class="accent-bar" style="top:170px" width="152" height="14"><polygon points="0,0 134,0 120,14 0,14" fill="var(--orange)"/><polygon points="134,0 152,0 152,14 120,14" fill="var(--red)"/></svg>
  <div class="body-text" style="left:164px;top:184px;width:243px">
    <h4>Increase Rapid Clinic Practice's Representation: Update Your Practice Specialty with the Registry Today</h4>
  </div>
  <div class="body-text" style="left:164px;top:214px;width:243px">
    <p>The National Physician Registry keeps records in their master file of all physicians in the United States, even if they are not registry members. Did you know that rapid clinic practice is one of the self-designated specialties? There is strength in numbers, so if you are not currently self-designated as practicing rapid clinic medicine as your primary or secondary specialty (you are allowed to list up to two specialties you practice), please call the registry now to correct this. Call 1-800-555-0199, select option "2" and then option "5", to speak to a registry representative and update your status.</p>
  </div>
  <div class="foot-band">
    <svg width="434" height="14"><rect width="434" height="14" fill="var(--orange)"/><polygon points="274,0 434,0 434,14 259,14" fill="var(--red)"/></svg>
    <span class="foot-label">INSTITUTE OF RAPID CLINIC PRACTICE</span>
  </div>
</section>

<section class="slide s-bells">
  <div class="top-band"></div>
  <div class="body-text" style="left:162px;top:68px;width:242px">
    Bell's palsy<br>
    Patient presented to the clinic with the classic signs of Bell's palsy. He had acute onset of left sided upper and lower facial paralysis resulting in facial droop and impaired eyelid closure. Bell's palsy is differentiated from a central process, because in Bell's palsy, the forehead and face are involved, whereas in a central process lesion (ie stroke), the forehead is spared. Though the exact cause of idiopathic Bell's palsy is unknown, providers will often treat the patient with corticosteroids in the acute phase to reduce inflammation and decrease time to recovery. HSV and other viral pathogens have been implicated as a possible cause, routine treatment with acyclovir or valacyclovir has not been shown to improve outcomes.<br>
    Mastoiditis<br>
    Mastoiditis is infection of the mastoid bone, and is a serious complication of ear infections, typically otitis media. Prior to antibiotics, mastoiditis was a frequent complication of acute otitis media. In this case, mastoiditis had progressed to involve the facial nerve, which caused the patient's Bell's palsy. This is a medical emergency and prompt referral to the Emergency Department or ENT specialist is critical. Risk factors for mastoiditis in adults include immunocompromised state and diabetes.<br>
    In closing, Bell's palsy is a common diagnosis in the clinic. The majority of patients with Bell's palsy will recover without medical intervention. However, be aware that more serious conditions such as mastoiditis may be lurking as a cause.
  </div>
  <svg class="accent-bar" width="152" height="14"><polygon points="0,0 134,0 120,14 0,14" fill="var(--orange)"/><polygon points="134,0 152,0 152,14 120,14" fill="var(--red)"/></svg>
  <div class="foot-band">
    <svg width="434" height="14"><rect width="434" height="14" fill="var(--orange)"/><polygon points="274,0 434,0 434,14 259,14" fill="var(--red)"/></svg>
    <span class="foot-label">INSTITUTE OF RAPID CLINIC PRACTICE</span>
  </div>
</section>

<section class="slide s-contact">
  <div class="top-band"></div>
  <div class="red-block" style="height:176px"></div>
  <div class="brand" style="left:152px;top:62px">
    <span class="brand-mark" style="width:22px;height:22px"></span>
    <span class="rule" style="position:static;width:1px;height:44px"></span>
    <span class="brand-name" style="font-size:10px">Institute of<br>Rapid Clinic<br>Practice</span>
  </div>
  <div class="about">
    The Institute of Rapid Clinic Practice (IRCP), formerly known as the Rapid Clinic College of Practitioners (RCCP), was founded by physicians from the Walk-In Care Alliance (WICA) to provide a physician voice for the specialty. IRCP and WICA continue to work closely to advance the clinical practice of rapid clinic medicine. In 2016 the RCCP board voted to include physician assistants and nurse practitioners as members. Thus in early 2017 the decision to change our name was made.
    <h3>Mission Statement</h3>
    We are rapid clinic clinicians elevating the quality of patient care and empowering our colleagues through education, advocacy, and research.
  </div>
  <ul class="contact-list">
    <li><svg width="13" height="13" viewBox="0 0 13 13"><circle cx="6.5" cy="6.5" r="6.5" fill="var(--red)"/><path d="M6.5 3a2 2 0 0 0-2 2c0 1.6 2 4 2 4s2-2.4 2-4a2 2 0 0 0-2-2z" fill="#fff"/></svg><span>4120 Meadow Crest Dr Suite 300<br>Lakeview, IL 60999</span></li>
    <li><svg width="13" height="13" viewBox="0 0 13 13"><circle cx="6.5" cy="6.5" r="6.5" fill="var(--red)"/><rect x="4.5" y="3" width="4" height="7" rx="0.8" fill="#fff"/></svg><span>PHONE: 1 800-555-0142</span></li>
    <li><svg width="13" height="13" viewBox="0 0 13 13"><circle cx="6.5" cy="6.5" r="6.5" fill="var(--red)"/><rect x="3.5" y="4.5" width="6" height="4.2" fill="#fff"/><path d="M3.5 4.5l3 2.3 3-2.3" stroke="var(--red)" stroke-width=".7" fill="none"/></svg><span>E-MAIL: INFO@IRCP-EDU.ORG</span></li>
    <li><svg width="13" height="13" viewBox="0 0 13 13"><circle cx="6.5" cy="6.5" r="6.5" fill="var(--red)"/></svg><span>@RapidClinicInst</span></li>
    <li><svg width="13" height="13" viewBox="0 0 13 13"><circle cx="6.5" cy="6.5" r="6.5" fill="var(--red)"/></svg><span>Follow us online</span></li>
  </ul>
  <div class="site-url">www.ircp-edu.org</div>
  <div class="foot-band">
    <svg width="438" height="14"><rect width="438" height="14" fill="var(--orange)"/><polygon points="276,0 438,0 438,14 261,14" fill="var(--red)"/></svg>
    <span class="foot-label">INSTITUTE OF RAPID CLINIC PRACTICE</span>
  </div>
</section>

<section class="slide s-member">
  <div class="top-band"></div>
  <div class="photo" role="img" aria-label="Portrait photo of the contributing clinician" style="left:35px;top:48px;width:117px;height:122px;background:linear-gradient(180deg,#e6e4e0,#cbbfb2 70%,#f3f3f3)"></div>
  <svg class="accent-bar" width="152" height="14"><polygon points="0,0 134,0 120,14 0,14" fill="var(--orange)"/><polygon points="134,0 152,0 152,14 120,14" fill="var(--red)"/></svg>
  <div class="body-text" style="left:164px;top:47px;width:243px">
    <div class="kicker">ANOTHER CASE FROM OUR MEMBERS</div>
    <div class="headline">Lyme disease strikes again</div>
    <p>22 year old male presents to the clinic with complaints of a lump on his back. He removed 2 other ticks this month and is suspicious it is a tick. He was landscaping his yard 2 days ago and working in the brush. He denies any complaints and vital signs are normal. On exam, an engorged Ixodes scapularis tick is found on his left upper back. It was removed without difficulty. The patient wants to know if he should take any medicine to prevent Lyme disease.</p>
    <p style="margin-top:6px">When our patients live in wooded areas and are often removing ticks, it is difficult to decide when to use prophylactic treatment. The Infection Guidance Council (IGC) has published clear guidelines for patients who live in endemic areas with tick exposures. Routine use of antibiotics or serologic testing is not recommended by IGC. The IGC recommends ALL criteria be met in order to be prescribed doxycycline single dose prophylaxis. Dosing for doxycycline for adults is 200 mg once or for children 8 years or greater 4 mg/kg up to 200 mg once. No alternative medications are recommended for pregnant patients, children less than 8 years old or doxycycline allergic patients currently.</p>
    <p style="margin-top:6px;text-align:left">1. Doxycycline is NOT contraindicated by the patient's medical history.<br>
    2. The tick was identified as an adult or nymph Ixodes scapularis tick.<br>
    3. The tick was attached equal to or greater than 36 hours decided upon by state of engorgement or reported exposure time.<br>
    4. Prophylaxis is within 72 hours of tick removal.<br>
    5. Lyme disease is common in the place of residence of the patient or area of exposure.</p>
  </div>
  <div class="foot-band">
    <svg width="434" height="14"><rect width="434" height="14" fill="var(--orange)"/><polygon points="274,0 434,0 434,14 259,14" fill="var(--red)"/></svg>
    <span class="foot-label">INSTITUTE OF RAPID CLINIC PRACTICE</span>
  </div>
</section>

<section class="slide s-title">
  <div class="top-band"></div>
  <div class="red-block" style="height:304px"></div>
  <span class="brand-mark" style="position:absolute;left:70px;top:104px;width:72px;height:72px;background:var(--orange)"></span>
  <span class="rule" style="left:169px;top:92px;width:2px;height:108px"></span>
  <div class="brand-name" style="position:absolute;left:184px;top:104px;font-size:27px;letter-spacing:1.5px;line-height:1.12">Institute of<br>Rapid Clinic<br>Practice</div>
  <div class="tagline">Elevating Care, Empowering Clinicians</div>
  <div class="foot-band">
    <svg width="438" height="14"><rect width="438" height="14" fill="var(--white)"/><polygon points="0,0 276,0 262,14 0,14" fill="var(--orange)"/></svg>
  </div>
</section>

</body>
</html>
```